Silver Hollow Dove Release Website Deisgn project

We need a website design for our dove release business.

We had several business cards designed awhile back....one for weddings and one for general releases (usually funerals). It was so hard to pick from all the great designs that were submitted. I have attached them.

We release white doves for all celebrations in life. Weddings, funerals, store openings, remembrance ceremonies, etc.

We need to appeal to brides and grooms as well as those grieving the loss of a loved one. It's a very delicate blend.

The name of our business is "Silver Hollow" and the name of our loft is "Marra's Roost". Our loft was established in 2012.

Target Market(s)

Brides, Grooms, Grieving Adults, Wedding Planners, Funeral Homes, Promoters

Industry/Entity Type

Professional Service

Number of Pages Required

5+ page

Font styles to use
Sans Serif

Requirements
Must have
• We will need some space for pictures I'm sure. We will need to have a contract & pricing page. We will need a contact us page.
• We need a more classic feel as we need to attract brides and those who are grieving. The solution may be a page for each......Wedding Releases & Funeral Releases & Other Celebrations
Nice to have
• If we have a page for each type of life celebration, there's more options for color. I would like the designer to choose the colors that are appropriate for the occasion.
• I would like to have a bit of decorative font in addition to the traditional website font.
Should not have
• We need to stay away from the yellow and orange colors.

```html
<!DOCTYPE html>
<html lang="en">
<head>
<meta charset="utf-8">
<title>Silver Hollow</title>
<link href="https://fonts.googleapis.com/css2?family=Lato:wght@400;700&family=Italianno&family=Cormorant+Garamond:ital,wght@1,500&display=swap" rel="stylesheet">
<style>
:root{
  --blue:#0a84cc;
  --blue-dark:#0567a8;
  --ink:#333;
  --muted:#555;
  --white:#fff;
  --footer:#3a3a3a;
  --icon:#2b2b2b;
}
*{margin:0;padding:0;box-sizing:border-box}
html,body{width:762px;height:1200px;overflow:hidden}
body{position:relative;font-family:"Lato",sans-serif;color:var(--ink);background:#fff}
.abs{position:absolute}
.topline{left:0;top:0;width:762px;height:3px;background:var(--blue)}
.brand{left:84px;top:24px;font-size:26px;font-weight:400;color:#222;letter-spacing:1px}
.mail{left:438px;top:8px;font-size:9px;color:#444;display:flex;align-items:center;gap:5px}
.phone{left:556px;top:0;width:120px;height:22px;background:var(--blue);border-radius:0 0 14px 14px;color:#fff;font-size:11px;font-weight:700;display:flex;align-items:center;justify-content:center;gap:4px}
.social{top:44px;width:20px;height:20px;border-radius:50%;background:var(--icon)}
.nav{left:0;top:76px;width:762px;height:29px;background:linear-gradient(#555,#333);display:flex;padding-left:84px}
.nav a{display:flex;align-items:center;justify-content:center;color:#fff;font-size:11.5px;font-weight:700;text-decoration:none;border-right:1px solid #666}
.nav a.active{background:linear-gradient(#6a6a6a,#4a4a4a)}
.hero{left:0;top:105px;width:762px;height:302px;overflow:hidden}
.caption{left:222px;top:318px;width:284px;height:89px;background:rgba(20,30,50,.78);color:#fff;font-family:"Cormorant Garamond",serif;font-style:italic;font-weight:500;font-size:20.5px;line-height:24px;text-align:center;padding-top:8px}
.arrow{top:237px;width:48px;height:29px;background:rgba(60,60,60,.6);display:flex;align-items:center;justify-content:center}
.arrow span{width:28px;height:26px;background:#333;display:flex;align-items:center;justify-content:center}
.band{left:0;top:407px;width:762px;height:106px;background:repeating-linear-gradient(45deg,#414141 0 2px,#383838 2px 4px)}
.cat-title{top:428px;width:200px;text-align:center;color:#fff;font-size:14px}
.cat-pic{top:457px;width:104px;height:104px;border-radius:50%;border:4px solid #fff;box-shadow:0 2px 5px rgba(0,0,0,.3)}
.script{font-family:"Italianno",cursive;color:#222;text-align:center;width:762px;left:0}
.welcome{top:580px;font-size:32px}
.intro{left:140px;top:629px;width:490px;font-size:8.6px;line-height:14.4px;text-align:center;color:var(--muted)}
.btn{left:344px;top:700px;width:86px;height:28px;border:1px solid #444;font-size:9.5px;display:flex;align-items:center;justify-content:center;color:#333}
.divider{left:0;top:740px;width:762px;height:20px;background:linear-gradient(#fff,#e6e6e6)}
.gallery-title{top:782px;font-size:32px}
.thumb{top:828px;width:143px;height:107px;border:3px solid #333;border-radius:3px}
.thumb.on{border-color:var(--blue)}
.thumb-cap{left:0;bottom:8px;width:100%;text-align:center;color:#fff;font-size:8.5px;font-weight:700;line-height:11px;text-shadow:0 1px 2px rgba(0,0,0,.6)}
.garrow{top:872px;font-size:18px;color:#222}
.footer-col h3{font-size:13px;font-weight:400;color:#fff;border-bottom:1px solid rgba(255,255,255,.4);padding-bottom:2px;margin-bottom:6px}
.footer-col{color:#fff;font-size:8px}
.links li{list-style:none;margin-bottom:9.5px}
.links li::before{content:"▸ ";font-size:7px}
.cd{display:flex;gap:8px;margin-bottom:11px;line-height:11px}
.copy{left:0;top:1177px;width:762px;height:23px;background:var(--footer);color:#fff;font-size:8px;display:flex;align-items:center;justify-content:center}
</style>
</head>
<body>
<div class="abs topline"></div>
<div class="abs brand">Silver Hollow</div>
<div class="abs mail"><svg width="12" height="8" viewBox="0 0 12 8"><rect width="12" height="8" fill="#0a84cc"/><path d="M0 0l6 5 6-5" stroke="#fff" fill="none"/></svg>info@silverhollow.com</div>
<div class="abs phone"><svg width="10" height="10" viewBox="0 0 10 10"><path d="M2 0l2 2-1 2c1 1 2 2 3 3l2-1 2 2-2 2C4 10 0 6 0 2z" fill="#fff"/></svg>555-210-4478</div>
<div class="abs social" style="left:574px" aria-label="Social link"></div>
<div class="abs social" style="left:601px" aria-label="Social link"></div>
<div class="abs social" style="left:628px" aria-label="Social link"></div>

<nav class="abs nav">
  <a class="active" style="width:99px">Home</a>
  <a style="width:131px">About Us</a>
  <a style="width:125px">Services</a>
  <a style="width:121px">Gallery</a>
  <a style="width:118px">Contact Us</a>
</nav>

<div class="abs hero">
  <svg width="762" height="302">
    <defs>
      <linearGradient id="h1" x1="0" y1="0" x2="0" y2="1"><stop offset="0" stop-color="#3d5a2a"/><stop offset=".6" stop-color="#6e8a4c"/><stop offset="1" stop-color="#d9dccf"/></linearGradient>
      <linearGradient id="h2" x1="1" y1="0" x2="0" y2="1"><stop offset="0" stop-color="#1f4c8f"/><stop offset=".5" stop-color="#5d95d6"/><stop offset="1" stop-color="#c9dcef"/></linearGradient>
      <linearGradient id="h3" x1="0" y1="0" x2="0" y2="1"><stop offset="0" stop-color="#7ea6dc"/><stop offset=".55" stop-color="#b9cde4"/><stop offset=".8" stop-color="#e8ecf1"/><stop offset="1" stop-color="#6f7d6a"/></linearGradient>
    </defs>
    <polygon points="0,0 268,0 220,302 0,302" fill="url(#h1)" role="img" aria-label="Bride and groom releasing white doves in a garden"/>
    <polygon points="268,0 541,0 495,302 220,302" fill="url(#h2)" role="img" aria-label="White dove flying in a bright blue sky"/>
    <polygon points="541,0 762,0 762,302 495,302" fill="url(#h3)" role="img" aria-label="Doves released over a white casket at a memorial"/>
  </svg>
</div>
<div class="abs caption">Ceremonial Dove Releases for<br>Wedding, Funerals, Celebrations<br>&amp; Memorials</div>
<div class="abs arrow" style="left:0"><span><svg width="8" height="10"><path d="M6 1L2 5l4 4" stroke="#fff" stroke-width="2" fill="none"/></svg></span></div>
<div class="abs arrow" style="left:714px"><span><svg width="8" height="10"><path d="M2 1l4 4-4 4" stroke="#fff" stroke-width="2" fill="none"/></svg></span></div>

<div class="abs band"></div>
<div class="abs cat-title" style="left:71px">Wedding Releases</div>
<div class="abs cat-title" style="left:280px">Funeral Releases</div>
<div class="abs cat-title" style="left:480px">Other Celebrations</div>
<div class="abs cat-pic" style="left:119px;background:radial-gradient(circle at 50% 40%,#f4f6f9,#c9d6e4 60%,#8fa3bd)" role="img" aria-label="Wedding couple releasing doves under a floral arch"></div>
<div class="abs cat-pic" style="left:329px;background:linear-gradient(#3d352f,#6a5f55 55%,#d9d9d6)" role="img" aria-label="Mourners releasing doves at a funeral"></div>
<div class="abs cat-pic" style="left:528px;background:linear-gradient(#4a5a3a,#7d8a68 55%,#c9c4b6)" role="img" aria-label="Family celebration with doves in flight"></div>

<div class="abs script welcome">Welcome To Silver Hollow</div>
<p class="abs intro">Lorem ipsum dolor sit amet, ex vim quem primis. Quot suavitate molestiae ex usu. Ridens eleifend ei sea, aeterno feugait molestie at eum, mel vitae principes sententiae an. Ex adolescens scripserit eam, per nisl laboramus ea. Cu est opulo senserit, te quem nonumy percipit cum.Invidunt molestiae qui in. Corpora iudicabit ius eu. Regione ceteros efficiantur ut quo. Semper labores accusam in eam.Graece ancillae pri id. Cu eos forensibus mediocritatem.</p>
<div class="abs btn">Read More</div>
<div class="abs divider"></div>

<div class="abs script gallery-title">Photo Gallery</div>
<div class="abs garrow" style="left:45px">‹</div>
<div class="abs garrow" style="left:706px">›</div>
<div class="abs thumb on" style="left:83px;background:linear-gradient(#dfe8f2,#b9cbe0 50%,#8c9fb8)" role="img" aria-label="Wedding party releasing doves"><div class="abs thumb-cap">Lorem ipsum dolor sit amet<br>ex vim quem primis</div></div>
<div class="abs thumb" style="left:234px;background:linear-gradient(#3f5a2c,#6b8a4c 55%,#e4e4dc)" role="img" aria-label="Bride and groom with doves among trees"></div>
<div class="abs thumb" style="left:384px;background:linear-gradient(#4f5a44,#7a7d6c 55%,#b8b2a4)" role="img" aria-label="Wedding guests on steps watching doves"></div>
<div class="abs thumb" style="left:535px;background:linear-gradient(#6b98d6,#a9c2e2 55%,#5a6b52)" role="img" aria-label="Doves released over a graveside service"></div>

<svg class="abs" style="left:0;top:945px" width="762" height="232">
  <defs><linearGradient id="fg" x1="0" y1="0" x2="0" y2="1"><stop offset="0" stop-color="#1f9be0"/><stop offset="1" stop-color="#0567a8"/></linearGradient></defs>
  <path d="M0 10 C120 110 400 110 762 40 L762 232 L0 232Z" fill="url(#fg)"/>
  <path d="M0 0 C100 95 400 100 762 25 L762 40 C400 110 120 110 0 20Z" fill="#3a3a3a"/>
</svg>

<div class="abs footer-col" style="left:83px;top:1050px;width:102px">
  <h3>Quick link</h3>
  <ul class="links"><li>Home</li><li>About Us</li><li>Services</li><li>Gallery</li><li>Contact Us</li></ul>
</div>
<div class="abs footer-col" style="left:233px;top:1050px;width:120px">
  <h3>Contact Details</h3>
  <div class="cd"><svg width="8" height="10"><path d="M4 0a4 4 0 014 4c0 3-4 6-4 6S0 7 0 4a4 4 0 014-4z" fill="#fff"/></svg><span>Lorem ipsum, dolor sit amet,<br>ex vim quem primis - 12345</span></div>
  <div class="cd"><svg width="9" height="9" viewBox="0 0 10 10"><path d="M2 0l2 2-1 2c1 1 2 2 3 3l2-1 2 2-2 2C4 10 0 6 0 2z" fill="#fff"/></svg><span>012.345.6789</span></div>
  <div class="cd"><svg width="9" height="9"><rect y="3" width="9" height="4" fill="#fff"/><rect x="2" width="5" height="9" fill="none" stroke="#fff"/></svg><span>012.345.6789</span></div>
  <div class="cd"><svg width="9" height="7"><rect width="9" height="7" fill="#fff"/><path d="M0 0l4.5 4 4.5-4" stroke="#0a84cc" fill="none"/></svg><span>info@silverhollow.com</span></div>
</div>
<div class="abs footer-col" style="left:401px;top:1048px;width:123px">
  <h3>Location Map</h3>
  <div style="width:123px;height:79px;background:linear-gradient(135deg,#f3efe2,#e8e2cf 60%,#f1e7b8)" role="img" aria-label="Street map showing the loft location"></div>
</div>
<div class="abs" style="left:578px;top:1125px;font-size:12px;color:rgba(255,255,255,.55)">Silver Hollow</div>

<div class="abs copy">Copyright © 2016 Silver Hollow. All Right Reserved</div>
</body>
</html>
```